Professional business card for an Actor

I'd like a professional business card I could give out to producers, and casting directors when meeting at an event. Here is the info I would like to have on my business card.

I am not sure 100% of what I want or how I want it so I am open to suggestions. I know I want something minimalistic. Clean. Straight forward. Something to make them want to find out more about me.

Here is what I'd want to be on the card:

- Full name: Tomas Velbrik (Maybe job: Actor or International Actor)
- My headshot photo is attached but I'm happy to see other options (You can find more photos in the gallery on my webpage www.tovelbrik.net but it should be a headshot)
- Webpage: www.tovelbrik.net (Perhaps a QR code to my site would be great??)
- Snapgrid username.
- Email
- Mobile number (with ChatLoop)

Optional/ideas:

- Languages spoken? English, Spanish, Galician, French, Portuguese.
- QR code to my showreel: https://reelhost.example/518204736
- Castfolio profile https://app.castfolio.example/5207-1938-4462 (QR code???)

The design of the business card should be clean and uncluttered, avoiding an excess of elements, or at least, well structured. I am just giving many ideas but I trust you to translate it into the card :)

- Style minimalistic but It could be something arty too. Whatever that means!

THANK YOU so much!!!!!
Updates

Nice to have

UPDATE: Thank you everyone for your submissions. Just for inspiration if this helps, I like some of the styles than can be found here: https://www.pinboardly.example/CardIdeasHub/performer-card-layouts/ Also. I would also be happy to see a version with Letterpress, Embossed printing or Thermorelief (See atttached images)

Should not have

UPDATE2: Please no white backgrounds. Great work everyone. I would suggest something like the style attached in the latest files. A reference for the style not the colours. THANK YOU!!!

Contact Information for Business Card

Details mentioned in the project description.

Requirements
Nice to have
• UPDATE: Thank you everyone for your submissions. Just for inspiration if this helps, I like some of the styles than can be found here: https://www.pinboardly.example/CardIdeasHub/performer-card-layouts/ Also. I would also be happy to see a version with Letterpress, Embossed printing or Thermorelief (See atttached images)
Should not have
• UPDATE2: Please no white backgrounds. Great work everyone. I would suggest something like the style attached in the latest files. A reference for the style not the colours. THANK YOU!!!

```html
<!DOCTYPE html>
<html lang="en">
<head>
<meta charset="utf-8">
<title>Tomas Velbrik – Business Card</title>
<link href="https://fonts.googleapis.com/css2?family=Poppins:wght@300;400;600&display=swap" rel="stylesheet">
<style>
  :root {
    --backdrop: #2b2b2c;
    --card-dark: #1c1d1f;
    --studio-grey-top: #505050;
    --studio-grey-low: #363636;
    --skin-warm: #c99a82;
    --hair-dark: #2a211d;
    --shirt-navy: #1b1c3a;
    --shirt-white: #ececec;
    --ink-white: #ffffff;
    --accent-coral: #f0675a;
    --rule-grey: #55565a;
  }
  * { margin: 0; padding: 0; box-sizing: border-box; }
  html, body { width: 1200px; height: 1108px; overflow: hidden; }
  body {
    background: var(--backdrop);
    font-family: "Poppins", sans-serif;
    position: relative;
  }
  .card {
    position: absolute;
    top: 209px;
    width: 430px;
    height: 690px;
    border-radius: 22px;
    overflow: hidden;
    box-shadow: 0 18px 40px rgba(0,0,0,0.45);
  }
  .card--front { left: 150px; }
  .card--back { left: 620px; background: var(--card-dark); }

  .headshot-fill {
    position: absolute; inset: 0;
    background:
      linear-gradient(180deg, transparent 0%, transparent 50%, var(--shirt-navy) 60%, var(--shirt-navy) 100%),
      radial-gradient(ellipse 34% 30% at 52% 38%, var(--skin-warm) 0%, rgba(201,154,130,0.75) 55%, transparent 100%),
      radial-gradient(ellipse 42% 22% at 52% 14%, var(--hair-dark) 0%, rgba(42,33,29,0.6) 60%, transparent 100%),
      radial-gradient(ellipse at 55% 30%, var(--studio-grey-top), var(--studio-grey-low) 75%);
  }
  .front-title {
    position: absolute; left: 0; right: 0; bottom: 92px;
    text-align: center;
  }
  .name {
    color: var(--ink-white);
    font-weight: 600;
    letter-spacing: 0.5px;
    line-height: 1.05;
    white-space: nowrap;
  }
  .front-title .name { font-size: 46px; }
  .role {
    color: var(--accent-coral);
    font-weight: 300;
    letter-spacing: 0.5px;
  }
  .front-title .role { font-size: 28px; margin-top: 6px; }

  .portrait-circle {
    position: absolute; top: 96px; left: 50%;
    width: 196px; height: 196px; margin-left: -98px;
    border-radius: 50%;
    background:
      radial-gradient(ellipse 60% 25% at 50% 100%, var(--shirt-white) 0%, var(--shirt-white) 60%, transparent 100%),
      radial-gradient(ellipse 30% 32% at 50% 52%, var(--skin-warm) 0%, rgba(201,154,130,0.7) 60%, transparent 100%),
      radial-gradient(ellipse 38% 20% at 50% 22%, var(--hair-dark) 0%, transparent 100%),
      radial-gradient(circle at 50% 40%, #6a6a6a, #4a4a4a 70%);
  }
  .back-title {
    position: absolute; top: 318px; left: 0; right: 0; text-align: center;
  }
  .back-title .name { font-size: 52px; }
  .back-title .role { font-size: 24px; margin-top: 2px; }

  .channel-row {
    position: absolute; top: 450px; left: 24px; right: 24px;
    display: flex; align-items: center; gap: 10px;
  }
  .channel-row .rule { flex: 1; height: 1px; background: var(--rule-grey); }
  .channel-icon { width: 36px; height: 36px; flex: none; }
  .channel-label {
    display: flex; align-items: center; gap: 5px;
    color: var(--accent-coral);
    font-size: 14px; font-weight: 400;
  }
  .channel-label .dot {
    width: 8px; height: 8px; border-radius: 50%; background: var(--accent-coral);
  }

  .contact-list {
    position: absolute; top: 506px; left: 0; right: 0;
    list-style: none; text-align: center;
    color: var(--ink-white);
    font-weight: 400;
    font-size: 23px;
    line-height: 1.65;
  }
</style>
</head>
<body>

<section class="card card--front">
  <div class="headshot-fill" role="img" aria-label="Headshot of Tomas Velbrik in a navy T-shirt against a grey studio backdrop"></div>
  <div class="front-title">
    <h1 class="name">Tomas Velbrik</h1>
    <p class="role">International Actor</p>
  </div>
</section>

<section class="card card--back">
  <div class="portrait-circle" role="img" aria-label="Smiling headshot of Tomas Velbrik in a white shirt"></div>
  <div class="back-title">
    <h2 class="name">Tomas Velbrik</h2>
    <p class="role">International Actor</p>
  </div>

  <div class="channel-row">
    <span class="rule"></span>
    <svg class="channel-icon" viewBox="0 0 36 36" aria-label="Phone">
      <circle cx="18" cy="18" r="16.5" fill="none" stroke="var(--accent-coral)" stroke-width="1.6"/>
      <path d="M13 11 l3 0 l1.5 4 l-2 1.5 a9 9 0 0 0 4 4 l1.5 -2 l4 1.5 l0 3 a2 2 0 0 1 -2 2 a14 14 0 0 1 -12 -12 a2 2 0 0 1 2 -2z" fill="none" stroke="var(--accent-coral)" stroke-width="1.6" stroke-linejoin="round"/>
    </svg>
    <svg class="channel-icon" viewBox="0 0 36 36" aria-label="Email">
      <circle cx="18" cy="18" r="16.5" fill="none" stroke="var(--accent-coral)" stroke-width="1.6"/>
      <rect x="10" y="12.5" width="16" height="11" rx="1" fill="var(--accent-coral)"/>
      <path d="M10.5 13 L18 19 L25.5 13" fill="none" stroke="var(--card-dark)" stroke-width="1.4"/>
    </svg>
    <svg class="channel-icon" viewBox="0 0 36 36" aria-label="Website">
      <circle cx="18" cy="18" r="16.5" fill="none" stroke="var(--accent-coral)" stroke-width="1.6"/>
      <g fill="none" stroke="var(--accent-coral)" stroke-width="1.4">
        <circle cx="18" cy="18" r="8"/>
        <ellipse cx="18" cy="18" rx="3.5" ry="8"/>
        <line x1="10" y1="18" x2="26" y2="18"/>
        <line x1="11.5" y1="14" x2="24.5" y2="14"/>
        <line x1="11.5" y1="22" x2="24.5" y2="22"/>
      </g>
    </svg>
    <span class="channel-label"><span class="dot"></span>Snapgrid</span>
    <span class="rule"></span>
  </div>

  <ul class="contact-list">
    <li>044-987 650 312</li>
    <li>tomasvelbrik@postbay.example</li>
    <li>www.tovelbrik.net</li>
    <li>/Tomas Velbrik</li>
  </ul>
</section>

</body>
</html>
```